Copperleaf Motorized Shade Business Card

Hello, we've had our logo made. Now we are looking for a clean and cool looking business card. One side can just be the logo with any design elements that might look good with it. The other side will be Name, Phone Number and Email. There will not be an address on the card.

```html
<!DOCTYPE html>
<html lang="en">
<head>
<meta charset="utf-8">
<title>Copperleaf Motorized Shade Business Card</title>
<link rel="stylesheet" href="https://fonts.googleapis.com/css2?family=Raleway:wght@600;700;800&display=swap">
<style>
  :root {
    --backdrop: #7a7c89;
    --card: #ffffff;
    --navy: #0b3c7a;
    --mint: #d9ecd5;
    --sky: #d3ebf8;
    --photo-top: #ddd6c8;
    --photo-mid: #eef0ea;
    --photo-low: #f4f4f0;
    --photo-accent: #c9b63c;
  }
  * { box-sizing: border-box; margin: 0; padding: 0; }
  html, body {
    width: 1200px; height: 792px; overflow: hidden;
    background: var(--backdrop);
    font-family: "Raleway", Arial, sans-serif;
  }
  .card {
    position: absolute; top: 136px;
    width: 302px; height: 523px;
    background: var(--card); overflow: hidden;
  }
  .card--front { left: 239px; }
  .card--back { left: 642px; }

  .front-photo {
    position: absolute; left: 26px; top: 30px;
    width: 250px; height: 465px;
    background: linear-gradient(180deg,
      var(--photo-top) 0%, #d6cfc0 40%,
      var(--photo-mid) 44%, var(--photo-low) 78%,
      var(--photo-accent) 84%, #d8d2b0 100%);
  }
  .front-wordmark {
    position: absolute; left: 0; right: 0; top: 275px;
    text-align: center; color: var(--navy);
    font-weight: 800; letter-spacing: 1px; line-height: 1.1;
  }
  .front-wordmark .wordmark-name { display: block; font-size: 30px; }
  .front-wordmark .wordmark-sub { display: block; font-size: 12px; letter-spacing: 4px; margin-top: 6px; }

  .back-band { position: absolute; left: 0; top: 0; width: 302px; height: 160px; }
  .back-wordmark {
    position: absolute; left: 162px; top: 102px; width: 104px;
    text-align: center; color: var(--navy); font-weight: 800; line-height: 1.1;
  }
  .back-wordmark .wordmark-name { display: block; font-size: 15px; letter-spacing: 0.5px; }
  .back-wordmark .wordmark-sub { display: block; font-size: 6px; letter-spacing: 1.6px; margin-top: 4px; }

  .rule { position: absolute; left: 50px; width: 55px; height: 2px; background: var(--navy); }
  .rule--top { top: 232px; }
  .rule--bottom { top: 295px; }
  .person-name {
    position: absolute; left: 50px; top: 245px;
    font-size: 17px; font-weight: 800; letter-spacing: 3px; color: var(--navy);
  }
  .person-title {
    position: absolute; left: 50px; top: 270px;
    font-size: 11px; font-weight: 700; letter-spacing: 2px; color: var(--navy);
  }
  .contact-block {
    position: absolute; left: 35px; top: 356px;
    width: 100px; height: 167px; background: var(--sky);
  }
  .contact-list { position: absolute; left: 50px; top: 398px; list-style: none; }
  .contact-list li {
    font-size: 11px; font-weight: 700; letter-spacing: 2.2px;
    color: var(--navy); height: 29.5px; white-space: nowrap;
  }
</style>
</head>
<body>
  <section class="card card--front">
    <div class="front-photo" role="img" aria-label="Photo of a woven roman shade over a bright window with a white bench and yellow cushions"></div>
    <div class="front-wordmark">
      <span class="wordmark-name">COPPERLEAF</span>
      <span class="wordmark-sub">MOTORIZED SHADE</span>
    </div>
  </section>

  <section class="card card--back">
    <svg class="back-band" viewBox="0 0 302 160" aria-hidden="true">
      <polygon points="0,0 302,0 302,153 0,112" fill="var(--mint)"/>
    </svg>
    <div class="back-wordmark">
      <span class="wordmark-name">COPPERLEAF</span>
      <span class="wordmark-sub">MOTORIZED SHADE</span>
    </div>

    <div class="rule rule--top"></div>
    <h1 class="person-name">YOUR NAME</h1>
    <p class="person-title">MANAGER</p>
    <div class="rule rule--bottom"></div>

    <div class="contact-block"></div>
    <ul class="contact-list">
      <li>582 - 317 - 946</li>
      <li>HELLO@COPPERLEAFSHADE.COM</li>
      <li>WWW.COPPERLEAFSHADE.COM</li>
    </ul>
  </section>
</body>
</html>
```